An innovative software company needs a business card!

We need a business card design for our new innovative software company. Please use the details for the business card provided in business card details section. We will use the business card paper like: https://www.plavex.com/us/products/nfc/business-cards-plus.html Our company name: kelvora We have already a logo and colors to use in business cards too ,

Target Market(s)

App & Sofware Development

Industry/Entity Type

Software

Contact Information for Business Card

Lukas Brenner, BSc.
Owner and Creative Superhero

Adress:
Tulpenweg 37/4/1809
A - 1100, Wien

Tel: +43 (0) 676 921 35 60
Email: lukas.brenner@kelvora.at
Web: www.kelvora.at

Requirements
Must have
• - Use our logo
Nice to have
• It would be nice to have a nice picture on the backside. (About apps, software, technicals or funy stuff) - Use our colors as in business card (optional)

```html
<!DOCTYPE html>
<html lang="en">
<head>
<meta charset="utf-8">
<title>kelvora business card</title>
<link rel="stylesheet" href="https://fonts.googleapis.com/css2?family=Montserrat:wght@300;400;500;700&display=swap">
<style>
  :root {
    --page: #e9ecef;
    --card-white: #fbfbfb;
    --cyan: #25b4cc;
    --cyan-light: #5fd0e0;
    --grey-swoosh: #d3d5d8;
    --grey-text: #a7abb0;
    --navy: #0d1a6b;
    --navy-mid: #1a3aa8;
    --map-cyan: #3cc3e6;
    --white: #ffffff;
  }
  * { margin: 0; padding: 0; box-sizing: border-box; }
  html, body { width: 1200px; height: 780px; overflow: hidden; }
  body {
    background: var(--page);
    font-family: "Montserrat", sans-serif;
    display: flex; align-items: center; justify-content: center; gap: 40px;
  }
  .card {
    position: relative; width: 550px; height: 314px;
    border-radius: 16px; overflow: hidden;
    box-shadow: 0 10px 28px rgba(0,0,0,.18);
  }
  .card-front { background: var(--card-white); }
  .card-front .wave { position: absolute; inset: 0; }
  .brand {
    position: absolute; left: 32px; top: 100px;
    display: flex; align-items: center; gap: 12px;
  }
  .brand-dot { width: 44px; height: 44px; border-radius: 50%; background: var(--cyan); flex: none; }
  .brand-name {
    font-weight: 700; font-size: 46px; color: var(--cyan); letter-spacing: -1px; line-height: 1;
  }
  .person { position: absolute; left: 36px; top: 180px; }
  .person-name { font-size: 18px; font-weight: 500; color: var(--cyan); }
  .person-title { font-size: 14px; font-weight: 300; color: var(--grey-text); margin-top: 2px; }
  .contact {
    position: absolute; right: 26px; top: 24px; text-align: right;
    color: var(--white); font-size: 13.5px; font-weight: 500; line-height: 1.5;
  }
  .contact-icons { display: flex; justify-content: flex-end; gap: 5px; margin-bottom: 14px; }
  .contact-icons svg { width: 18px; height: 18px; }
  .contact-address { margin-bottom: 16px; }

  .card-back {
    background: linear-gradient(135deg, var(--navy-mid), var(--navy) 75%);
  }
  .back-city {
    position: absolute; left: 0; top: 0; width: 150px; height: 100%;
    background: linear-gradient(180deg, rgba(26,58,168,.2), rgba(40,90,200,.7));
  }
  .back-map {
    position: absolute; left: 150px; top: 20px; width: 380px; height: 270px;
    border-radius: 40% 30% 45% 35%;
    background: radial-gradient(ellipse at 45% 45%, var(--map-cyan), rgba(60,195,230,.35) 60%, transparent 78%);
  }
  .back-brand {
    position: absolute; left: 28px; top: 28px; display: flex; align-items: center; gap: 12px;
  }
  .back-brand .brand-dot { width: 40px; height: 40px; background: var(--white); }
  .back-brand .brand-name { color: var(--white); font-size: 46px; }
  .back-web {
    position: absolute; right: 28px; bottom: 24px;
    color: var(--white); font-size: 14px; font-weight: 500;
  }
</style>
</head>
<body>
  <section class="card card-front">
    <svg class="wave" viewBox="0 0 550 314" preserveAspectRatio="none">
      <path d="M185 314 C 245 260, 280 200, 300 150 C 315 110, 330 60, 360 0 L 550 0 L 550 314 Z" fill="var(--grey-swoosh)"/>
      <path d="M235 314 C 300 250, 300 180, 312 120 C 322 60, 352 20, 390 0 L 550 0 L 550 314 Z" fill="var(--card-white)"/>
      <path d="M255 314 C 320 250, 322 170, 335 110 C 348 50, 375 18, 410 0 L 550 0 L 550 314 Z" fill="var(--cyan)"/>
      <path d="M330 314 C 360 270, 360 190, 375 130 C 390 70, 420 25, 460 0 L 470 0 C 430 30, 410 80, 400 140 C 388 210, 380 270, 350 314 Z" fill="var(--cyan-light)" opacity=".45"/>
    </svg>
    <div class="brand">
      <div class="brand-dot"></div>
      <div class="brand-name">kelvora</div>
    </div>
    <div class="person">
      <div class="person-name">Lukas Brenner, BSc.</div>
      <div class="person-title">Owner and Creative Superhero</div>
    </div>
    <div class="contact">
      <div class="contact-icons">
        <svg viewBox="0 0 18 18"><rect width="18" height="18" rx="3" fill="var(--white)"/><path d="M4 9.5 L7.5 13 L14 5.5" stroke="var(--cyan)" stroke-width="2.2" fill="none"/></svg>
        <svg viewBox="0 0 18 18"><rect width="18" height="18" rx="3" fill="var(--white)"/><rect x="4" y="5.5" width="10" height="7" fill="none" stroke="var(--cyan)" stroke-width="1.6"/><path d="M4 5.5 L9 10 L14 5.5" stroke="var(--cyan)" stroke-width="1.6" fill="none"/></svg>
        <svg viewBox="0 0 18 18"><rect width="18" height="18" rx="3" fill="var(--white)"/><circle cx="9" cy="9" r="5" fill="none" stroke="var(--cyan)" stroke-width="1.5"/><path d="M4 9 H14 M9 4 C6 7,6 11,9 14 M9 4 C12 7,12 11,9 14" stroke="var(--cyan)" stroke-width="1.1" fill="none"/></svg>
      </div>
      <div class="contact-address">Tulpenweg 37/4/1809<br>A - 1100, Wien</div>
      <div>+43 (0) 676 921 35 60</div>
      <div>lukas.brenner@kelvora.at</div>
      <div>www.kelvora.at</div>
    </div>
  </section>

  <section class="card card-back">
    <div class="back-city" role="img" aria-label="Night city skyline photograph in blue tones"></div>
    <div class="back-map" role="img" aria-label="Glowing world map with connection lines"></div>
    <div class="back-brand">
      <div class="brand-dot"></div>
      <div class="brand-name">kelvora</div>
    </div>
    <div class="back-web">www.kelvora.at</div>
  </section>
</body>
</html>
```